RM Tomás Rivera (Business Card)

Hi designers, in this work, I'm looking for an sophisticated stylish, elegant and proffesional personal card. We have a laboratory of pathology automated, with equipments high quality.
In this web the designers, have created my business logo, the name is "RM Tomás Rivera"
In our lab, we principal work is to prepare the biopsies for further diagnostic of diseases like cancer, tumors, etc.
I need that the first face, only having my complete logo (Rm Tomás Rivera, Laboratorio de procesamiento Histologico)
The overleaf, could repeat the same logo, like water logo.
In this face, I need to say: My full data:

Técnico en Anatomía Patológica
Tomás Rivera Ibarra M.P 47203
Av. Paredes Luján 418 - 2do piso - Instituto Marbel.
Córdoba, Argentina
(0351) 154820937
rivera.tomas@correolab.example

with respect the colors of card, use your imagination, the original logo color is violet, I haven't chosen a color base for the card.

attached pictures are examples of cards I like your DESIGN.
Attached too, the original logo to my company.

the size of card are:
horizontal: 9cm
vertical: 5,5cm

any question that you have, not doubt to question me,
Hand to work!

Industry/Entity Type

Laboratory

Requirements
Must have
• designers sophisticated, not simples, like show the images attached

```html
<!DOCTYPE html>
<html lang="es">
<head>
<meta charset="utf-8">
<title>Tomás Rivera — Tarjeta personal</title>
<link href="https://fonts.googleapis.com/css2?family=Open+Sans:wght@400;600&family=Roboto+Condensed:wght@400&display=swap" rel="stylesheet">
<style>
  :root {
    --violet: #5b2a91;
    --violet-light: #7440b0;
    --grey: #7b7d80;
    --ink: #1d1d1f;
    --paper: #ffffff;
    --stage: #e9e6e2;
  }
  * { margin: 0; padding: 0; box-sizing: border-box; }
  html, body { width: 1200px; height: 1023px; overflow: hidden; background: var(--stage); }
  .stage { position: relative; width: 1200px; height: 1023px; }
  .card {
    position: absolute; top: 346px; width: 540px; height: 330px; overflow: hidden;
    box-shadow: 0 10px 24px rgba(0,0,0,.18);
    font-family: "Open Sans", Arial, sans-serif;
  }
  .card--front { left: 40px; background: var(--paper); }
  .card--back { left: 620px; background: linear-gradient(135deg, var(--violet-light), var(--violet)); }
  .card__waves { position: absolute; inset: 0; }

  .brand { position: absolute; text-align: center; }
  .brand__mark { display: flex; align-items: center; justify-content: center; gap: 10px; }
  .brand__dot { width: 14px; height: 14px; border-radius: 50%; }
  .brand__name { font-family: "Roboto Condensed", Arial, sans-serif; letter-spacing: .35em; white-space: nowrap; }
  .brand__rule { height: 1px; margin: 6px auto; }
  .brand__tagline { font-family: "Roboto Condensed", Arial, sans-serif; white-space: nowrap; }

  .card--front .brand { top: 24px; left: 110px; width: 270px; }
  .card--front .brand__dot { background: var(--violet); }
  .card--front .brand__name { font-size: 15px; color: var(--violet); }
  .card--front .brand__rule { background: var(--grey); width: 100%; }
  .card--front .brand__tagline { font-size: 13.5px; color: var(--ink); }

  .licence { position: absolute; left: 26px; top: 26px; font-size: 11px; color: var(--grey); }
  .licence span { color: var(--violet); }

  .address { position: absolute; left: 160px; top: 92px; display: flex; gap: 6px; font-size: 9.5px; line-height: 1.4; color: var(--ink); text-transform: uppercase; white-space: nowrap; }
  .address svg { flex: none; margin-top: 2px; }

  .holder { position: absolute; left: 30px; top: 148px; }
  .holder__name { font-size: 25px; color: var(--ink); font-weight: 400; line-height: 1.2; }
  .holder__title { font-size: 12px; color: var(--violet); }

  .contact { position: absolute; left: 30px; bottom: 18px; list-style: none; color: var(--paper); font-size: 13px; }
  .contact li { display: flex; align-items: center; gap: 8px; margin-top: 4px; }

  .card--back .brand { top: 92px; left: 50%; transform: translateX(-50%); width: 360px; }
  .card--back .brand__dot { background: var(--paper); width: 18px; height: 18px; }
  .card--back .brand__name { font-size: 22px; color: var(--paper); }
  .card--back .brand__rule { background: var(--paper); width: 100%; }
  .card--back .brand__tagline { font-size: 19px; color: var(--paper); }
</style>
</head>
<body>
<main class="stage">

  <section class="card card--front" aria-label="Tarjeta, cara de datos">
    <svg class="card__waves" width="540" height="330" viewBox="0 0 540 330" aria-hidden="true">
      <path d="M540 70 C450 85 380 125 300 180 C385 140 455 108 540 96 Z" fill="var(--grey)"/>
      <path d="M0 262 C120 262 220 225 300 186 C380 146 455 118 540 110 L540 330 L0 330 Z" fill="var(--violet)"/>
    </svg>

    <p class="licence">PRN <span>M.P 47203</span></p>

    <div class="brand">
      <div class="brand__mark"><span class="brand__dot"></span><span class="brand__name">TOMÁS RIVERA</span></div>
      <div class="brand__rule"></div>
      <p class="brand__tagline">LABORATORIO DE PROCESAMIENTO HISTOLOGICO</p>
    </div>

    <div class="address">
      <svg width="9" height="12" viewBox="0 0 9 12"><path d="M4.5 0A4.5 4.5 0 0 0 0 4.5C0 8 4.5 12 4.5 12S9 8 9 4.5A4.5 4.5 0 0 0 4.5 0Zm0 6.3a1.8 1.8 0 1 1 0-3.6 1.8 1.8 0 0 1 0 3.6Z" fill="var(--ink)"/></svg>
      <p>Av. Paredes Luján 418 - 2do piso -<br>Instituto Marbel. Córdoba, Argentina</p>
    </div>

    <div class="holder">
      <h1 class="holder__name">Tomás Rivera</h1>
      <p class="holder__title">Técnico en Anatomía Patológica</p>
    </div>

    <ul class="contact">
      <li><svg width="10" height="13" viewBox="0 0 10 13"><rect x="1" y="0.5" width="8" height="12" rx="1.5" fill="none" stroke="#fff"/></svg>(0351) 154820937</li>
      <li><svg width="13" height="10" viewBox="0 0 13 10"><rect width="13" height="10" fill="#fff"/><path d="M0 0 L6.5 5.5 L13 0" fill="none" stroke="var(--violet)"/></svg>rivera.tomas@correolab.example</li>
    </ul>
  </section>

  <section class="card card--back" aria-label="Tarjeta, cara de marca">
    <svg class="card__waves" width="540" height="330" viewBox="0 0 540 330" aria-hidden="true">
      <path d="M-20 250 C120 180 300 330 560 200" fill="none" stroke="rgba(255,255,255,.07)" stroke-width="40"/>
      <path d="M-20 60 C140 10 330 140 560 40" fill="none" stroke="rgba(255,255,255,.06)" stroke-width="30"/>
    </svg>
    <div class="brand">
      <div class="brand__mark"><span class="brand__dot"></span><span class="brand__name">TOMÁS RIVERA</span></div>
      <div class="brand__rule"></div>
      <p class="brand__tagline">LABORATORIO DE PROCESAMIENTO HISTOLOGICO</p>
    </div>
  </section>

</main>
</body>
</html>
```